" Empresa jovem, em franca expansao, com necessidade de ampliar e qualificar sua carteira de clientes, buscando aprimorar sua identidade visual para se destacar em uma concorrência com pouco investimento nesse fundamento corporativo e potencializar sua apresentaçao a clientes de grande porte. "

```html
<!DOCTYPE html>
<html lang="pt-BR">
<head>
<meta charset="utf-8">
<title>Afiadora Laminora — Pasta institucional</title>
<link rel="stylesheet" href="https://fonts.googleapis.com/css2?family=Montserrat:wght@400;600;800&display=swap">
<style>
  :root {
    --navy: #0e3558;
    --green: #1f9e4c;
    --paper: #ffffff;
    --paper-shade: #f2f3f4;
    --faint: #e6e8ea;
    --backdrop: #d9d6d2;
    --hole: #9aa3ab;
    --label: #5b6b78;
  }
  html, body {
    margin: 0;
    width: 1200px;
    height: 1200px;
    overflow: hidden;
    background: var(--backdrop);
    font-family: "Montserrat", sans-serif;
  }
  .folder {
    position: absolute;
    left: 96px;
    top: 127px;
    width: 1014px;
    height: 880px;
  }
  .panel-back {
    position: absolute;
    left: 0; top: 0;
    width: 507px; height: 880px;
    background: var(--navy);
  }
  .panel-front {
    position: absolute;
    left: 507px; top: 0;
    width: 507px; height: 880px;
    background: var(--paper);
    overflow: hidden;
  }
  .front-motif {
    position: absolute;
    left: 19px; top: 110px;
    width: 430px; height: 400px;
    background: linear-gradient(135deg, var(--paper) 0%, var(--faint) 45%, var(--faint) 70%, var(--paper) 100%);
  }
  .brand-square {
    position: absolute;
    left: 348px; top: 520px;
    width: 58px; height: 58px;
    background: var(--navy);
  }
  .brand-label {
    position: absolute;
    left: 262px; top: 588px;
    width: 234px;
    text-align: center;
    font-weight: 600;
    font-size: 13px;
    letter-spacing: 9px;
    color: var(--label);
  }
  .brand-name {
    position: absolute;
    left: 250px; top: 604px;
    width: 250px;
    text-align: center;
    font-weight: 800;
    font-size: 38px;
    letter-spacing: 1px;
    line-height: 1;
    color: var(--navy);
    white-space: nowrap;
  }
  .hole {
    position: absolute;
    left: 477px;
    width: 56px; height: 56px;
    border: 2px solid var(--hole);
    border-radius: 50%;
    box-sizing: border-box;
    background: var(--paper);
  }
  .hole-top { top: 229px; }
  .hole-bottom { top: 618px; }
  .back-footer {
    position: absolute;
    left: 0; top: 710px;
    width: 507px;
    text-align: center;
    color: var(--paper);
  }
  .back-footer .footer-name {
    font-weight: 800;
    font-size: 13px;
    letter-spacing: 1px;
  }
  .back-footer .footer-address {
    margin-top: 18px;
    font-size: 9px;
  }
  .back-footer .footer-web {
    margin-top: 10px;
    font-size: 9px;
  }
  .pocket {
    position: absolute;
    left: -43px; top: 790px;
    width: 550px; height: 140px;
  }
  .pocket-side {
    position: absolute;
    left: 0; top: 10px;
    width: 43px; height: 130px;
    background: var(--paper-shade);
  }
  .pocket-band {
    position: absolute;
    left: 43px; top: 10px;
    width: 507px; height: 130px;
    background: var(--green);
  }
  .pocket-tab {
    position: absolute;
    left: 115px; top: 0;
    width: 385px; height: 14px;
    background: var(--green);
    border-radius: 10px 10px 0 0;
  }
  .card-slot {
    position: absolute;
    left: 68px; top: 46px;
    width: 130px; height: 70px;
    border: 2px solid rgba(255,255,255,0.55);
    border-radius: 8px;
    box-sizing: border-box;
  }
</style>
</head>
<body>
  <main class="folder">
    <section class="panel-back">
      <div class="back-footer">
        <div class="footer-name">LAMINORA</div>
        <div class="footer-address">Rua das Oficinas, 120 Centro - Vale Alto - MG - 31 4000-1200</div>
        <div class="footer-web">www.laminora.com.br</div>
      </div>
    </section>
    <section class="panel-front">
      <div class="front-motif" role="img" aria-label="Grande elemento gráfico geométrico da marca em cinza claro"></div>
      <span class="brand-square"></span>
      <div class="brand-label">AFIADORA</div>
      <div class="brand-name">LAMINORA</div>
    </section>
    <span class="hole hole-top"></span>
    <span class="hole hole-bottom"></span>
    <div class="pocket">
      <div class="pocket-side"></div>
      <div class="pocket-tab"></div>
      <div class="pocket-band">
        <div class="card-slot"></div>
      </div>
    </div>
  </main>
</body>
</html>
```